Card Game Design - 5 Faces Only (Islamic Geometry Inspired)

The idea behind this project is to design a set a cards for a game. The game works as follows:

1 - Everyday you start with a deck of cards
2 - As the day progresses each card contains an action to perform
3 - If you perform that action, you move the card, face-up, to the pack of the deck
4 - If you do not perform that action, you flip the card over and place it at the back of the deck.
5 - At the end of the day, you review your deck.

The front of each card contains 3 major elements:

1 - Title
2 - Value - ie a number, score for completing the act
3 - An encouraging statement

The back of each card contains 3 elements:

1 - Title
2 - Value - ie a number, essentially a “minus” number
3 - A calligraphic symbol that will take-up of most of the card.

The back of the card is a simpler single design. The front of the card is slightly more complex. The front cards need to be of four types. The difference in types should preferably be in both color and design changes that indicate the four types.

Thus, the designer will be designing essentially 5 card faces. The back is the same for all designs, but the front four can either be variations in color / form or both.

The front facing cards are of the following types:

1 - Prayer - these are the cards that will reflect a prayer to be performed
2 - Day - these will be cards with actions to be performed on Monday, Thursday and Friday
3 - Awrād - activities that are to be performed on a daily basis
4 - Daily - activities that are to be performed on a daily basis

Overall Design Ethic

Modern board games have beautifully designed cards that are uniquely branded. The overall ethos of these cards are that they should reflect traditional Islamic art in nature. Think beautiful designed geometric patterns and calligraphy. If one can weave these design elements in a card face that is beautifully showcases the main elements - title, point and statement - that would be ideal.For this design project,

I am looking to get the 5 cards in PSDs ready for printing. I will add the front facing text and the text for the reverse except for the calligraphic panel that is linked below. Nevertheless, sample fonts and texts should be provided so that overall harmony with the design can be effectively assessed.

The calligraphic symbol for the back can be found here:

https://www.pelvarin-find.example/results?q=brush+script+panel&set=img&ref=A1b2C3d4E5f6G7h8

A circular version and square version that show in the display are very appealing. Other versions can be used if assessed to have a better fit for the design.

Alternatively, a calligraphic rendering of the phrase "Astaghfirullah" can also be used. Samples here:

https://www.pelvarin-find.example/results?q=ink+phrase+lettering&set=img&ref=H9i8J7k6L5m4N3o2

Sample Design Ethos

https://www.pelvarin-find.example/results?q=framed+panel&set=img&ref=P1q2R3s4T5u6V7w8

https://www.pelvarin-find.example/results?set=img&q=gilded+manuscript+borders&ref=X9y8Z7a6B5c4D3e2F1g0h9

https://www.pelvarin-find.example/results?set=img&q=ornate+tile+motifs&ref=J1k2L3m4N5o6P7q8R9s0#view=_

https://www.pelvarin-find.example/results?q=star+lattice+patterns&set=img&ref=T1u2V3w4X5y6Z7a8

Board Game Ethos

https://www.pelvarin-find.example/results?set=img&q=tabletop+card+layouts&ref=B1c2D3e4F5g6H7i8J9k0

Font styles to use
Serif
Sans Serif

Requirements
Must have
• Elegant, unified design.
• Must be aesthetically pleasing.
• Beautiful and vivid coloring without being gaudy.
Nice to have
• Meaningful symbolism.
• For example: Two small circles in each top corner of the card. One with a stylized representation of the Tolvenne and the other the Spire of the Keeper's hall in Madinah.
• See: https://www.quillmarsh-stock.example/browse/stone+cube+shrine?page=3&layout=vertical&licensed=true&filter=safe&origin=related_browse
• See: https://www.pelvarin-find.example/results?q=brenhollow+college&set=img&ref=Q1w2E3r4T5y6U7i8O9p0A1s2D3f4G5h6J7k8L9z0X1c2V3b4N5m6

```html
<!DOCTYPE html>
<html lang="en">
<head>
<meta charset="utf-8">
<title>Sadaqah — Action Card</title>
<link rel="stylesheet" href="https://fonts.googleapis.com/css2?family=Cinzel:wght@500;600;700&family=Tinos:wght@700&display=swap">
<style>
  :root {
    --card-deep: #1f0730;
    --card-mid: #33104a;
    --gold-light: #ffd23a;
    --gold: #f5b300;
    --gold-dark: #c97d00;
    --text-gold: #f8ba0c;
  }
  * { box-sizing: border-box; margin: 0; padding: 0; }
  html, body {
    width: 771px;
    height: 1200px;
    overflow: hidden;
    background: var(--card-deep);
  }
  .card {
    position: relative;
    width: 771px;
    height: 1200px;
    overflow: hidden;
    background: radial-gradient(ellipse at 50% 48%, var(--card-mid) 0%, #280a3c 55%, var(--card-deep) 100%);
  }
  .card-frame {
    position: absolute;
    inset: 0;
    width: 771px;
    height: 1200px;
  }
  .card-title {
    position: absolute;
    left: 0;
    right: 0;
    top: 226px;
    text-align: center;
    font-family: "Cinzel", serif;
    font-weight: 500;
    font-size: 66px;
    letter-spacing: 0.42em;
    padding-left: 0.42em;
    color: var(--text-gold);
    line-height: 1;
  }
  .card-value {
    position: absolute;
    left: 180px;
    top: 368px;
    width: 411px;
    height: 420px;
    display: flex;
    align-items: center;
    justify-content: center;
    font-family: "Tinos", serif;
    font-weight: 700;
    font-size: 182px;
    line-height: 1;
    color: var(--gold);
    background: linear-gradient(180deg, var(--gold-light) 20%, var(--gold) 55%, var(--gold-dark) 100%);
    -webkit-background-clip: text;
    background-clip: text;
    -webkit-text-fill-color: transparent;
    filter: drop-shadow(0 3px 2px rgba(0,0,0,0.45));
  }
  .card-statement {
    position: absolute;
    left: 0;
    right: 0;
    top: 834px;
    text-align: center;
    font-family: "Cinzel", serif;
    font-weight: 600;
    font-size: 46px;
    line-height: 57px;
    letter-spacing: 0.02em;
    color: var(--text-gold);
  }
</style>
</head>
<body>
  <main class="card">
    <svg class="card-frame" viewBox="0 0 771 1200" xmlns="http://www.w3.org/2000/svg" aria-hidden="false">
      <defs>
        <linearGradient id="gold-band" x1="0" y1="0" x2="1" y2="1">
          <stop offset="0" stop-color="#ffd23a"/>
          <stop offset="0.5" stop-color="#f5b300"/>
          <stop offset="1" stop-color="#d98900"/>
        </linearGradient>
      </defs>

      <!-- outer frame band -->
      <rect class="outer-band" x="38" y="60" width="695" height="1080" rx="18" fill="none" stroke="url(#gold-band)" stroke-width="20"/>
      <rect class="outer-inner-line" x="56" y="78" width="659" height="1044" rx="10" fill="none" stroke="#f5b300" stroke-width="3"/>

      <!-- corner ornaments -->
      <g role="img" aria-label="Gilded interlaced corner ornament, top left">
        <rect x="24" y="46" width="160" height="118" rx="14" fill="url(#gold-band)"/>
      </g>
      <g role="img" aria-label="Gilded interlaced corner ornament, top right">
        <rect x="587" y="46" width="160" height="118" rx="14" fill="url(#gold-band)"/>
      </g>
      <g role="img" aria-label="Gilded interlaced corner ornament, bottom left">
        <rect x="24" y="1036" width="160" height="118" rx="14" fill="url(#gold-band)"/>
      </g>
      <g role="img" aria-label="Gilded interlaced corner ornament, bottom right">
        <rect x="587" y="1036" width="160" height="118" rx="14" fill="url(#gold-band)"/>
      </g>

      <!-- small flourishes -->
      <g role="img" aria-label="Gold scrollwork flourish above the title">
        <rect x="250" y="130" width="271" height="26" rx="13" fill="#e9a400" opacity="0.85"/>
      </g>
      <g role="img" aria-label="Gold scrollwork flourish below the statement">
        <rect x="250" y="1054" width="271" height="26" rx="13" fill="#e9a400" opacity="0.85"/>
      </g>

      <!-- value panel frame -->
      <rect class="value-frame" x="182" y="370" width="407" height="416" fill="none" stroke="url(#gold-band)" stroke-width="6"/>
      <rect class="value-frame-inner" x="194" y="382" width="383" height="392" fill="none" stroke="#f5b300" stroke-width="2"/>
      <g role="img" aria-label="Filigree corner ornaments of the value panel">
        <rect x="194" y="382" width="78" height="78" fill="#e9a400" opacity="0.55"/>
        <rect x="499" y="382" width="78" height="78" fill="#e9a400" opacity="0.55"/>
        <rect x="194" y="696" width="78" height="78" fill="#e9a400" opacity="0.55"/>
        <rect x="499" y="696" width="78" height="78" fill="#e9a400" opacity="0.55"/>
      </g>
    </svg>

    <h1 class="card-title">SADAQAH</h1>
    <div class="card-value">+2</div>
    <p class="card-statement">Giving in sadaqah<br>does not decrease<br>your wealth</p>
  </main>
</body>
</html>
```